Business Card Design Project

Beauty Therapist
Bold, bright, feminine, like contrast, love flowers, girly stuff. Must be beautiful. But open to all suggestions. Business name: Plucky Plum.
xxx
Dorota Kaczmarczyk
Updates

Project Deadline Extended
Reason: I think you need more time to design something good. X

Target Market(s)

ignore this

Industry/Entity Type

Business

```html
<!DOCTYPE html>
<html lang="en">
<head>
<meta charset="utf-8">
<title>Plucky Plum – Business Cards</title>
<link rel="stylesheet" href="https://fonts.googleapis.com/css2?family=Ubuntu:wght@300;400;700&display=swap">
<style>
  :root {
    --page: #e9e4df;
    --plum-deep: #4a0f3a;
    --plum: #7a1a5e;
    --magenta: #a8246f;
    --pink-glow: #d9779f;
    --pink-soft: #e9a6c2;
    --ink-light: #ffffff;
    --ink-muted: rgba(255,255,255,0.85);
    --rule: rgba(255,255,255,0.7);
  }
  * { margin: 0; padding: 0; box-sizing: border-box; }
  html, body { width: 1200px; height: 1023px; overflow: hidden; }
  body {
    background: var(--page);
    font-family: "Ubuntu", sans-serif;
    display: flex;
    flex-direction: column;
    align-items: center;
    justify-content: center;
    gap: 36px;
  }
  .card {
    position: relative;
    width: 800px;
    height: 457px;
    border-radius: 4px;
    overflow: hidden;
    color: var(--ink-light);
    box-shadow: 0 10px 28px rgba(60,20,50,0.28);
  }
  .card-pattern {
    position: absolute;
    inset: 0;
    background:
      radial-gradient(ellipse 55% 60% at 88% 10%, var(--pink-soft) 0%, var(--pink-glow) 30%, rgba(217,119,159,0) 70%),
      radial-gradient(ellipse 70% 70% at 55% 45%, var(--magenta) 0%, rgba(168,36,111,0) 75%),
      linear-gradient(135deg, var(--plum) 0%, var(--magenta) 45%, var(--plum) 75%, var(--plum-deep) 100%);
  }
  .brand-name {
    font-weight: 300;
    color: var(--ink-light);
    letter-spacing: 1px;
    line-height: 1;
  }

  /* Front */
  .card-front .front-brand {
    position: absolute;
    left: 130px;
    top: 150px;
  }
  .card-front .brand-name { font-size: 104px; }
  .card-front .tagline {
    display: block;
    text-align: right;
    font-size: 22px;
    font-weight: 300;
    margin-top: 8px;
    color: var(--ink-muted);
  }
  .card-front .website {
    position: absolute;
    left: 420px;
    top: 330px;
    font-size: 22px;
    font-weight: 300;
    letter-spacing: 2px;
  }

  /* Back */
  .card-back .back-brand {
    position: absolute;
    left: 470px;
    top: 48px;
  }
  .card-back .brand-name { display: block; font-size: 72px; }
  .card-back .brand-name + .brand-name { margin-left: 40px; }
  .card-back .tagline {
    display: block;
    margin: 8px 0 0 44px;
    font-size: 20px;
    font-weight: 300;
    color: var(--ink-muted);
  }
  .card-back .divider {
    position: absolute;
    left: 440px;
    top: 30px;
    width: 1px;
    height: 200px;
    background: var(--rule);
  }
  .card-back .divider-h {
    position: absolute;
    left: 270px;
    top: 148px;
    width: 170px;
    height: 1px;
    background: var(--rule);
  }
  .contact {
    position: absolute;
    left: 150px;
    top: 210px;
    width: 270px;
    font-size: 22px;
    font-weight: 300;
    line-height: 1.5;
  }
  .contact .person-first { font-weight: 700; font-size: 24px; }
  .contact .person-last { font-size: 24px; margin-bottom: 10px; }
</style>
</head>
<body>
  <section class="card card-back">
    <div class="card-pattern" role="img" aria-label="Magenta background with soft scattered rounded-square pattern"></div>
    <div class="divider"></div>
    <div class="divider-h"></div>
    <div class="back-brand">
      <span class="brand-name">plucky</span>
      <span class="brand-name">plum</span>
      <span class="tagline">beauty therapist</span>
    </div>
    <div class="contact">
      <p class="person-first">Dorota</p>
      <p class="person-last">Kaczmarczyk</p>
      <p class="phone">123.456.7890</p>
      <p class="email">email@yourwebsite.com</p>
      <p class="web">www.yourwebsite.com</p>
    </div>
  </section>

  <section class="card card-front">
    <div class="card-pattern" role="img" aria-label="Magenta background with soft scattered rounded-square pattern"></div>
    <div class="front-brand">
      <span class="brand-name">pluckyplum</span>
      <span class="tagline">beauty therapist</span>
    </div>
    <p class="website">www.yourwebsite.com</p>
  </section>
</body>
</html>
```